Flyer-Design für Neueröffnung feinKragen
Zielgruppe
Wir bieten Marken Hemden und Accessoires unter anderem von den Herstellern Faltenmeister, Lumira und Veltrano in unserem Ladengeschäft sowie online in unserem Shop.
Unsere Zielgruppe ist der anspruchsvolle Mann, gut gebildet, aufstrebend und modebewusst, das ist das typische Bild unserer Zielgruppe.
Kunden können von uns ein modisches Hemd in hervorragender Qualität und exzellentem Service erwarten.
Aufgabenstellung
Feiern Sie mit uns die
NEU ERÖFFNUNG
Endlich in Oberkochen Markenhemden in großer Auswahl.
Am Samstag, 01. April 09:00-16:00Uhr
20% auf Alles - kein Aprilscherz
www.feinKragen.de
(Texte könne auch verändert werden, außer die Fakten - Neueröffnung - Datum - 20% auf alles)

```html
<!DOCTYPE html>
<html lang="de">
<head>
<meta charset="utf-8">
<title>feinKragen – Neueröffnung</title>
<link rel="stylesheet" href="https://fonts.googleapis.com/css2?family=Exo+2:wght@400;500;700;800&display=swap">
<style>
  :root {
    --sky-light: #c9e0e6;
    --sky: #b3d3dc;
    --sky-deep: #9ec6d3;
    --shirt-white: #eef4f6;
    --aubergine: #4f2045;
    --badge-dark: #52233f;
    --badge-rim: #8b6a86;
    --ink: #1c1c1c;
    --white: #ffffff;
  }
  * { margin: 0; padding: 0; box-sizing: border-box; }
  html, body { width: 1200px; height: 848px; overflow: hidden; }
  body { font-family: "Exo 2", sans-serif; color: var(--ink); }

  .flyer {
    position: relative;
    width: 1200px;
    height: 848px;
    overflow: hidden;
    background: linear-gradient(100deg, var(--sky-light) 0%, var(--sky) 55%, var(--sky-deep) 100%);
  }

  .hero-photo {
    position: absolute;
    left: 410px;
    top: 0;
    width: 790px;
    height: 848px;
    background: linear-gradient(180deg, rgba(238,244,246,0) 0%, rgba(238,244,246,0) 55%, rgba(238,244,246,0.55) 100%);
  }

  .frame {
    position: absolute;
    inset: 12px;
    border: 2px solid rgba(255,255,255,0.75);
    pointer-events: none;
  }

  .intro {
    position: absolute;
    left: 70px;
    top: 87px;
    font-size: 25px;
    font-weight: 400;
  }

  .headline {
    position: absolute;
    left: 64px;
    top: 120px;
    font-size: 63px;
    font-weight: 800;
    letter-spacing: 0.3px;
    color: var(--aubergine);
    line-height: 1.1;
  }

  .offer {
    position: absolute;
    left: 67px;
    top: 195px;
    font-size: 25px;
    letter-spacing: 0.3px;
    line-height: 31px;
  }

  .facts {
    position: absolute;
    left: 65px;
    top: 326px;
    font-size: 28px;
    line-height: 36px;
  }
  .facts .row { display: flex; margin-bottom: 13px; }
  .facts .label { width: 101px; font-weight: 700; }

  .brand {
    position: absolute;
    left: 55px;
    top: 712px;
    display: flex;
    align-items: center;
    gap: 14px;
    color: var(--aubergine);
  }
  .brand-dot {
    width: 50px;
    height: 50px;
    border-radius: 50%;
    background: var(--aubergine);
  }
  .brand-name {
    font-size: 44px;
    font-weight: 400;
    letter-spacing: 14px;
  }

  .web {
    position: absolute;
    left: 49px;
    top: 785px;
    font-size: 27px;
    letter-spacing: 0.5px;
    color: var(--aubergine);
  }

  .discount-badge {
    position: absolute;
    left: 860px;
    top: 481px;
    width: 290px;
    height: 290px;
  }
</style>
</head>
<body>
<main class="flyer">
  <div class="hero-photo" role="img" aria-label="Foto: lächelnder Mann im weißen Hemd vor hellblauem Hintergrund"></div>
  <div class="frame"></div>

  <p class="intro">Feiern Sie mit uns die</p>
  <h1 class="headline">NEUERÖFFNUNG!</h1>
  <p class="offer">
    Endlich in Oberkochen<br>
    Markenhemden in großer Auswahl.<br>
    (Faltenmeister, Lumira und Veltrano u.v.m.)
  </p>

  <div class="facts">
    <div class="row"><span class="label">WO?</span><span>Musterstrasse 111,<br>73447 Oberkochen</span></div>
    <div class="row"><span class="label">Wann?</span><span>Am Samstag, 01. April<br>09:00-16:00 Uhr</span></div>
  </div>

  <div class="brand">
    <span class="brand-dot"></span>
    <span class="brand-name">feinKragen</span>
  </div>
  <p class="web">www.feinKragen.de</p>

  <svg class="discount-badge" viewBox="0 0 290 290" aria-label="20 % auf Alles! Kein Aprilscherz">
    <circle cx="145" cy="145" r="132" fill="var(--badge-rim)"/>
    <circle cx="145" cy="145" r="132" fill="none" stroke="var(--badge-rim)" stroke-width="22"
            stroke-linecap="round" stroke-dasharray="0 23.04"/>
    <circle cx="145" cy="145" r="123" fill="var(--badge-dark)"/>
    <circle cx="145" cy="145" r="121" fill="none" stroke="var(--white)" stroke-width="1.2" opacity="0.85"/>
    <text x="145" y="124" text-anchor="middle" fill="var(--white)" font-family="'Exo 2', sans-serif" font-weight="700" font-size="74">20 %</text>
    <text x="145" y="176" text-anchor="middle" fill="var(--white)" font-family="'Exo 2', sans-serif" font-weight="700" font-size="42">auf Alles!</text>
    <text x="145" y="212" text-anchor="middle" fill="var(--white)" font-family="'Exo 2', sans-serif" font-weight="400" font-size="19">Kein Aprilscherz</text>
  </svg>
</main>
</body>
</html>
```